Specialized tax accounting firm needs marketing postcard

We need a postcard design for a professional services firm called R. Desmond Plork Inc. The firm is essentially a very specialized tax accounting firm - instead of serving the end consumer, we support other public accounting firms in the area of Canadian and U.S. tax advisory and compliance (i.e. they call us on tax issues too complex for the general practitioner). Our byline is "Tax Support Services for Public Accounting Firms". Our postcard should utilize our logo and be based on colours present in our logo (see file attached). The final design needs to convey professionalism and trustworthiness (we're hired by accountants after all!) while being creative and eye-catching. Eye-catching is critical, since many prospective recipients will not have heard from me before and I want them to read the postcard.

I've attached:
The font used in the logo
The logo itself in a variety of file formats
A picture of myself for incorporation in the postcard
A sample postcard from Publisher showing the wording to be used in the postcard and the elements to be included

Please note that in including a draft postcard I don't want the designer to follow the layout as is. It just shows the basic elements I want included. The only element which should remain constant is the wording - I do want the text elements included as written - however, everything else - font, size, placement of elements, etc. is up for creative ideas.

Please note that there is much more leather background around the logo than needs to be incorporated in the letterhead.

Industry/Entity Type

Accounting

```html
<!DOCTYPE html>
<html lang="en">
<head>
<meta charset="utf-8">
<title>R. Desmond Plork Inc. – Postcard</title>
<link href="https://fonts.googleapis.com/css2?family=Cinzel:wght@500&family=Tinos:wght@400;700&display=swap" rel="stylesheet">
<style>
  :root {
    --stage: #3b3b3b;
    --paper: #ffffff;
    --band-blue: #d6e8f8;
    --panel-blue: #e6f0fa;
    --ink: #1a1a1a;
    --leather-dark: #121212;
    --leather-mid: #262626;
    --gold: #f0a42a;
    --logo-blue: #2f78b8;
    --text-light: #f2f2f2;
    --rule: #cfcfcf;
  }
  * { box-sizing: border-box; margin: 0; padding: 0; }
  html, body { width: 1200px; height: 800px; overflow: hidden; }
  body {
    position: relative;
    background: var(--stage);
    font-family: "Tinos", "Times New Roman", serif;
    color: var(--ink);
  }

  /* Back of card */
  .card-back {
    position: absolute; left: 28px; top: 18px;
    width: 620px; height: 480px;
    background: var(--paper);
  }
  .intro-band {
    position: absolute; left: 0; top: 0; width: 620px; height: 154px;
    background: var(--band-blue);
  }
  .intro-text {
    position: absolute; left: 29px; top: 26px; width: 434px;
    font-size: 15px; line-height: 18.5px; text-align: justify;
  }
  .address-panel {
    position: absolute; left: 476px; top: 26px; width: 120px; height: 116px;
    background: var(--panel-blue);
  }
  .services-block {
    position: absolute; left: 0; top: 154px; width: 300px; height: 242px;
    background: var(--band-blue);
    padding: 4px 15px 0 29px;
    font-size: 15px; line-height: 18.5px;
  }
  .services-block p { text-align: justify; }
  .services-block p + p { margin-top: 18.5px; text-align: left; }

  /* Front of card */
  .card-front {
    position: absolute; left: 558px; top: 302px;
    width: 620px; height: 480px;
    background: radial-gradient(ellipse at 40% 35%, var(--leather-mid), var(--leather-dark) 80%);
    color: var(--text-light);
    overflow: hidden;
  }
  .portrait {
    position: absolute; left: 342px; top: 28px; width: 278px; height: 452px;
    background: linear-gradient(180deg, #2a2a2a 0%, #3a3533 40%, #1c1c1c 100%);
  }
  .brand {
    position: absolute; left: 39px; top: 48px; width: 380px; height: 56px;
  }
  .brand-mark {
    position: absolute; left: 0; top: 0; width: 52px; height: 52px;
    background: var(--logo-blue);
  }
  .brand-name {
    position: absolute; left: 62px; top: -2px;
    font-family: "Cinzel", "Times New Roman", serif; font-weight: 500;
    font-size: 31px; letter-spacing: 1px; color: var(--text-light);
    white-space: nowrap;
  }
  .brand-inc {
    position: absolute; left: 62px; top: 32px; width: 318px;
    display: flex; align-items: center; gap: 8px;
    font-family: "Cinzel", serif; font-size: 10px; color: var(--text-light);
  }
  .brand-inc::before, .brand-inc::after {
    content: ""; flex: 1; height: 1px; background: var(--rule);
  }
  .brand-tagline {
    position: absolute; left: 62px; top: 44px; width: 318px;
    font-family: "Tinos", serif; font-size: 10px; letter-spacing: 0.6px;
    text-transform: uppercase; color: var(--text-light); white-space: nowrap;
  }
  .headline {
    position: absolute; left: 30px; top: 118px; width: 430px;
    text-align: center; color: var(--gold);
    font-family: "Tinos", serif; font-weight: 400;
    font-size: 24px; line-height: 32px; letter-spacing: 0.6px;
    text-transform: uppercase;
  }
  .body-copy {
    position: absolute; left: 39px; top: 192px; width: 316px;
    font-size: 15px; line-height: 18.2px;
  }
  .body-copy p + p { margin-top: 18px; }
  .contact-row {
    position: absolute; left: 37px; top: 434px; width: 560px;
    display: flex; justify-content: space-between;
    font-size: 14px;
  }
  .contact-item { display: flex; align-items: center; gap: 6px; }
  .contact-item svg { width: 15px; height: 15px; fill: var(--gold); }
</style>
</head>
<body>

<section class="card-back">
  <div class="intro-band"></div>
  <p class="intro-text"><strong>R. Desmond Plork Inc.</strong> is a boutique tax accounting firm specializing in tax support for public accounting firms. Our support services cover a range of Canadian tax advisory and compliance needs - tax research and opinions, review of complex personal and corporate compliance, the design and execution of special tax projects such as corporate reorganizations or the purchase and sale of businesses.</p>
  <div class="address-panel"></div>
  <div class="services-block">
    <p>In addition to our support services for public accounting firms, we also provide Canadian and U.S. tax advisory and compliance services to the general public. We specialize in helping people with international tax issues – U.S. citizens living in Canada, people emigrating from or immigrating to Canada, non-residents disposing of Canadian real estate.</p>
    <p>Please feel free to contact me if I can be of assistance to you or to your clients.</p>
  </div>
</section>

<section class="card-front">
  <div class="portrait" role="img" aria-label="Portrait photograph of the firm's principal in a dark suit, arms crossed"></div>

  <div class="brand">
    <div class="brand-mark"></div>
    <div class="brand-name">R. DESMOND PLORK</div>
    <div class="brand-inc">INC</div>
    <div class="brand-tagline">Tax Support Services for Public Accounting Firms</div>
  </div>

  <h1 class="headline">Do your clients need<br>help with their U.S. taxes?</h1>

  <div class="body-copy">
    <p>You probably know that U.S. citizens have to file U.S. tax returns every year—even if they live in Canada. So do your clients. That’s why they’re asking you if you know anyone who can help them with their U.S. filings.</p>
    <p>Finding a tax accountant who can help with U.S. filings is tough. U.S. tax preparers have to be registered with the IRS to be eligible to prepare U.S. returns. Your client needs someone with experience, someone timely, someone charging a reasonable price. With a proven track record of over 15 years, I can deliver.</p>
  </div>

  <div class="contact-row">
    <span class="contact-item">
      <svg viewBox="0 0 16 16" aria-hidden="true"><path d="M2 5c0-2 2-3 6-3s6 1 6 3v1h-3V5H5v1H2z"/><rect x="3" y="7" width="10" height="7" rx="1"/></svg>
      902.555.0148
    </span>
    <span class="contact-item">
      <svg viewBox="0 0 16 16" aria-hidden="true"><path d="M1 3h14v10H1z M1 3l7 6 7-6" stroke="#121212" stroke-width="1"/></svg>
      desmond@plorktax.services
    </span>
    <span class="contact-item">
      <svg viewBox="0 0 16 16" aria-hidden="true"><circle cx="8" cy="8" r="7"/><path d="M1 8h14M8 1v14M3 4h10M3 12h10" stroke="#121212" stroke-width="1" fill="none"/><ellipse cx="8" cy="8" rx="3" ry="7" stroke="#121212" stroke-width="1" fill="none"/></svg>
      www.plorktax.services
    </span>
  </div>
</section>

</body>
</html>
```